Selka Marrow Photography Business Card

I need a new business card/ possibly design to use for other marking materials ... I have included my logo below in a few different colors, but can also provide the logo in additional colors and sizes. I would love a card the expresses clean, simple and classy.

Target Market(s)

Portrait photography clients, child photography clients

Industry/Entity Type

Photographer

Contact Information for Business Card

Selka Marrow Photography, Braintree MA, www.selkamarrowphotography.example
T. 555-283-9146 E. selkamarrowphoto@mailbox.example

Colors
33b8a4
eea4c8
5c5c5c

Requirements
Must have
• I would like to include my logo on card.
Nice to have
• I also like the color brown as well as the choices below. I would like a simple, elegant card, something classy.

```html
<!DOCTYPE html>
<html lang="en">
<head>
<meta charset="utf-8">
<title>Selka Marrow Photography — Business Card</title>
<link rel="stylesheet" href="https://fonts.googleapis.com/css2?family=Arimo:wght@400;700&display=swap">
<style>
  :root {
    --teal: #55b7ab;
    --teal-deep: #2f6f67;
    --ink: #1e1e1e;
    --paper: #ffffff;
    --backdrop: #e9e6e1;
  }
  * { box-sizing: border-box; margin: 0; padding: 0; }
  html, body { width: 1200px; height: 900px; overflow: hidden; }
  body {
    background: var(--backdrop);
    font-family: "Arimo", Arial, sans-serif;
    display: flex;
    align-items: center;
    justify-content: center;
    gap: 40px;
  }
  .card {
    width: 540px;
    height: 300px;
    position: relative;
    box-shadow: 0 6px 18px rgba(0,0,0,0.12);
    overflow: hidden;
  }

  /* Front */
  .card-front {
    background: var(--teal);
    display: flex;
    align-items: center;
    justify-content: center;
  }
  .brand-name {
    color: var(--teal-deep);
    font-weight: 400;
    font-size: 30px;
    letter-spacing: 0.04em;
    text-align: center;
    line-height: 1.35;
  }
  .brand-name span { display: block; font-size: 15px; letter-spacing: 0.35em; }

  /* Back */
  .card-back { background: var(--paper); }
  .name-tab {
    position: absolute;
    left: 0; top: 0;
    width: 250px;
    height: 60px;
    background: var(--teal);
    border-radius: 0 0 6px 0;
    color: var(--paper);
    padding: 8px 0 0 38px;
  }
  .name-tab .person { font-size: 19px; line-height: 1.1; }
  .name-tab .role { font-size: 12px; }
  .contact-list {
    position: absolute;
    left: 14px; top: 72px;
    list-style: none;
    font-size: 13px;
    color: var(--ink);
    line-height: 1.25;
  }
  .contact-list li { display: flex; align-items: center; gap: 8px; margin-bottom: 6px; }
  .contact-list svg { width: 18px; height: 16px; flex: none; }
  .web-line { position: absolute; left: 14px; bottom: 20px; font-size: 13px; color: var(--ink); }
  .mini-brand {
    position: absolute;
    right: 26px; top: 130px;
    color: var(--teal);
    font-size: 13px;
    text-align: center;
    line-height: 1.2;
  }
  .mini-brand span { display: block; font-size: 7px; letter-spacing: 0.3em; }
</style>
</head>
<body>
  <section class="card card-front" aria-label="Card front">
    <p class="brand-name">Selka Marrow<span>PHOTOGRAPHY</span></p>
  </section>

  <section class="card card-back" aria-label="Card back">
    <div class="name-tab">
      <p class="person">Selka Marrow</p>
      <p class="role">Lead Photographer</p>
    </div>
    <ul class="contact-list">
      <li>
        <svg viewBox="0 0 18 16" aria-hidden="true"><path d="M9 1 1 8h2.5v7h4v-4h3v4h4V8H17z" fill="var(--teal)"/></svg>
        Suite 12, 48 Elm Row, Braintree MA
      </li>
      <li>
        <svg viewBox="0 0 18 16" aria-hidden="true"><path d="M2 5c0-2 3-3 7-3s7 1 7 3v2h-4V5.5H6V7H2z" fill="var(--teal)"/><rect x="4" y="8" width="10" height="7" rx="1.5" fill="var(--teal)"/></svg>
        555-283-9146
      </li>
      <li>
        <svg viewBox="0 0 18 16" aria-hidden="true"><rect x="3" y="2" width="12" height="12" fill="none" stroke="var(--teal)" stroke-width="1.5"/></svg>
        555-283-9147
      </li>
      <li>
        <svg viewBox="0 0 18 16" aria-hidden="true"><rect x="1.5" y="3" width="15" height="10" fill="none" stroke="var(--teal)" stroke-width="1.5"/><path d="M1.5 3 9 9l7.5-6" fill="none" stroke="var(--teal)" stroke-width="1.5"/></svg>
        Email: selkamarrowphoto@mailbox.example
      </li>
      <li>
        <svg viewBox="0 0 18 16" aria-hidden="true"><circle cx="9" cy="8" r="7" fill="var(--teal)"/><path d="M2 8h14M9 1c-3 4-3 10 0 14M9 1c3 4 3 10 0 14" fill="none" stroke="var(--paper)" stroke-width="1"/></svg>
        www.selkamarrowphotography.example
      </li>
    </ul>
    <p class="mini-brand">Selka Marrow<span>PHOTOGRAPHY</span></p>
  </section>
</body>
</html>
```